Design and Renovation Company Luxury Business Card

I want to create a luxury business card for a Design and Renovation Firm . We will use our current logo. The company name is 742KAVO. We do not want anything standard. We need a very unique concept.
Please see uploaded inspiration. I really like the textured paper option. I would like the card to be thick with debossing, and/or embossing options. The logo has orange in it but I would like to see the card with and without the orange. I think the orange may make the company feel less high-end. The goal is to elevate the logo not match its vibe per se of the logo. We want something very unique, not standard at all!
I would like a space for :
Logo,
Name,
Position,
Email,
Office number,
Website Address,
Business Address,
Thank you!
Have fun!
Target Market(s)
Home owners Age 35 +
Industry/Entity Type
Design and Renovation
Contact Information for Business Card
Logo, Name, Position, Email, Office number, Website Address, Business Address,.
Colors
Designer to choose colors to be used in the design.
Requirements
Must have
- A luxury designer feel. Must be black or dark grey but open to other luxury ideas.
Nice to have
- Gold, silver, black embossing or debossing. Textured paper design.
Should not have
- A cheap look and feel.

```html
<!DOCTYPE html>
<html lang="en">
<head>
<meta charset="utf-8">
<title>742KAVO Business Card</title>
<link href="https://fonts.googleapis.com/css2?family=Quicksand:wght@400;500&display=swap" rel="stylesheet">
<style>
  :root {
    --page: #ffffff;
    --card-black: #0d0f11;
    --card-edge: #060708;
    --quilt-light: #2a3136;
    --quilt-dark: #0a0c0e;
    --gold: #d8b45a;
    --text-font: "Quicksand", sans-serif;
  }
  * { margin: 0; padding: 0; box-sizing: border-box; }
  html, body {
    width: 1200px;
    height: 586px;
    overflow: hidden;
    background: var(--page);
  }
  .sheet {
    position: relative;
    width: 1200px;
    height: 586px;
  }
  .card {
    position: absolute;
    top: 119px;
    width: 538px;
    height: 348px;
    overflow: hidden;
    font-family: var(--text-font);
    color: var(--gold);
  }
  .card--front { left: 46px; }
  .card--back {
    left: 617px;
    background: radial-gradient(ellipse at 45% 45%, #1a1d20 0%, var(--card-black) 65%, var(--card-edge) 100%);
  }
  .quilted-texture {
    position: absolute;
    inset: 0;
    background: radial-gradient(ellipse at 40% 35%, var(--quilt-light) 0%, #161b1f 50%, var(--quilt-dark) 100%);
  }
  .brand-name {
    position: absolute;
    inset: 0;
    display: flex;
    align-items: center;
    justify-content: center;
    font-weight: 500;
    font-size: 34px;
    letter-spacing: 5px;
    line-height: 1;
  }
  .contact__name {
    position: absolute;
    left: 20px;
    top: 12px;
    font-size: 25px;
    font-weight: 400;
    letter-spacing: 3px;
  }
  .contact__list {
    position: absolute;
    left: 20px;
    top: 72px;
    font-size: 16.5px;
    font-weight: 400;
    letter-spacing: 1.6px;
    line-height: 26.5px;
  }
  .contact__address {
    margin-top: 4px;
    line-height: 22.5px;
  }
  .contact__web {
    position: absolute;
    right: 18px;
    bottom: 17px;
    font-size: 16px;
    letter-spacing: 2.4px;
  }
</style>
</head>
<body>
  <main class="sheet">
    <section class="card card--front">
      <div class="quilted-texture" role="img" aria-label="Dark quilted diamond-pattern paper texture"></div>
      <p class="brand-name">742KAVO</p>
    </section>

    <section class="card card--back">
      <p class="contact__name">Name</p>
      <div class="contact__list">
        <p>Position</p>
        <p>info@742kavo.com</p>
        <p>+905 555 0147</p>
        <p class="contact__address">27 Harlow Vale Parkway<br>Brookmere, Ontario Canada<br>L0X 2B7</p>
      </div>
      <p class="contact__web">www.742kavo.ca</p>
    </section>
  </main>
</body>
</html>
```